Business card design to suit our website

Need a nice looking business card for our business based off images from our Website and provided images. The business card will require 2 different names (for the 2 owners). The business card should include images from our website, facebook (larkvale coil starter pack) or the pictures provided. it should also contain all contact information.
Our website is www.larkvalecoilworks.com.au
Please dont use image from top bar of website. If images are used please use the ones of our product under the buy it now tab
Updates

Need extra days to review

Target Market(s)

Automotive

Industry/Entity Type

Automotive Part

Contact Information for Business Card

Business Name. contact details including names phone number email. logo
2 business cards needed with 2 different persons names and phone number.

Colors

Designer to choose colors to be used in the design.

Requirements
Must have
• whatever looks best

```html
<!DOCTYPE html>
<html lang="en">
<head>
<meta charset="utf-8">
<title>Larkvale Coil Starter Pack – Business Card</title>
<link rel="stylesheet" href="https://fonts.googleapis.com/css2?family=Roboto:wght@400;700;900&display=swap">
<style>
  :root{
    --red:#c41e2f;
    --ink:#1a1a1a;
    --grey:#8a8a8a;
    --white:#ffffff;
    --stage:#d9d9d9;
    --gold:#c9a23a;
  }
  *{box-sizing:border-box;margin:0;padding:0}
  html,body{width:1200px;height:880px;overflow:hidden}
  body{background:var(--stage);font-family:"Roboto",Arial,sans-serif;color:var(--ink);position:relative}
  .card{position:absolute;width:700px;height:400px;background:var(--white);border-radius:22px;overflow:hidden;box-shadow:0 6px 18px rgba(0,0,0,.18)}
  .card--front{left:40px;top:30px}
  .card--back{left:460px;top:450px}
  .band{position:absolute;left:0;top:0;width:700px;height:400px}
  .tread{position:absolute;background:linear-gradient(90deg,rgba(200,200,200,0),rgba(200,200,200,.55) 40%,rgba(200,200,200,.2))}

  /* logo lockup */
  .brand{position:absolute;color:var(--red);font-weight:900;line-height:1}
  .brand__origin{display:block;font-size:15px;color:var(--ink);font-weight:700;margin-bottom:4px}
  .brand__name{display:flex;align-items:center;gap:10px;font-size:58px;letter-spacing:-1px}
  .brand__mark{width:22px;height:22px;border-radius:50%;background:var(--red)}
  .brand__tag{display:block;font-size:19px;color:var(--grey);font-weight:700;margin-top:4px;margin-left:32px}

  /* front */
  .car-art{position:absolute;left:0;top:40px;width:370px;height:330px;background:linear-gradient(135deg,#f2f2f2 0%,#bdbdbd 45%,#8d8d8d 75%,#d7d7d7 100%)}
  .card--front .brand{left:380px;top:28px}
  .contact{position:absolute;left:400px;top:146px}
  .contact__name{font-size:24px;font-weight:700;line-height:1.15}
  .contact__role{font-size:15px;color:var(--red);font-weight:700;margin-bottom:8px}
  .contact__line{display:flex;align-items:center;gap:8px;font-size:15px;margin-top:5px}
  .icon{width:22px;height:22px;border-radius:50%;background:var(--red);display:flex;align-items:center;justify-content:center}
  .callout{position:absolute;right:34px;bottom:26px;color:var(--white);font-size:22px;font-weight:700}

  /* back */
  .gallery{position:absolute;left:24px;top:18px;width:652px;height:240px}
  .panel{position:absolute;border:4px solid var(--red);background:var(--white)}
  .panel__photo{position:absolute;inset:12px;border-radius:4px}
  .panel--kit{left:0;top:50px;width:215px;height:190px}
  .panel--tool{left:211px;top:50px;width:215px;height:190px}
  .panel--pack{left:422px;top:0;width:230px;height:150px}
  .photo--kit{background:radial-gradient(circle at 45% 50%,#d8d8d8,#f7f7f7 70%)}
  .photo--tool{background:radial-gradient(circle at 55% 45%,#6b6b6b,#cfcfcf 55%,#fafafa 80%)}
  .photo--pack{background:linear-gradient(135deg,#b8323f,#e3c9cc 60%,#8a1b26)}
  .card--back .brand{left:462px;top:178px}
  .card--back .brand__name{font-size:44px;gap:8px}
  .card--back .brand__mark{width:18px;height:18px}
  .card--back .brand__origin{font-size:13px}
  .card--back .brand__tag{font-size:16px;margin-left:26px}
  .badge{position:absolute;left:40px;top:274px;width:80px;height:80px;border-radius:50%;background:radial-gradient(circle,#f4d77a,var(--gold) 60%,#8c6b1d);box-shadow:0 0 0 5px #e8c860}
  .fitment{position:absolute;left:150px;top:270px;font-size:16px;line-height:1.25}
  .fitment strong{display:block;font-size:20px}
  .site{position:absolute;right:40px;bottom:18px;color:var(--white);font-size:19px;font-weight:700}
</style>
</head>
<body>

<section class="card card--front">
  <div class="tread" style="left:240px;top:20px;width:460px;height:70px"></div>
  <div class="car-art" role="img" aria-label="Pencil-style illustration of a silver sedan front with a chequered flag behind"></div>
  <svg class="band" viewBox="0 0 700 400" aria-hidden="true">
    <path d="M0 360 C200 350 330 345 420 330 L700 300 L700 400 L0 400 Z" fill="var(--red)"/>
    <path d="M0 352 C200 342 330 337 420 322 L700 292" fill="none" stroke="var(--ink)" stroke-width="3"/>
  </svg>
  <div class="brand">
    <span class="brand__origin">Made In Australia</span>
    <span class="brand__name"><span class="brand__mark"></span>Larkvale</span>
    <span class="brand__tag">Coil Starter Pack</span>
  </div>
  <div class="contact">
    <div class="contact__name">Dorian Welles</div>
    <div class="contact__role">President</div>
    <div class="contact__line"><span class="icon"><svg width="12" height="12" viewBox="0 0 12 12"><rect x="3" y="1" width="6" height="10" rx="1" fill="none" stroke="#fff" stroke-width="1.4"/></svg></span>0491 570 156</div>
    <div class="contact__line"><span class="icon"><svg width="12" height="12" viewBox="0 0 12 12"><rect x="1" y="3" width="10" height="7" fill="none" stroke="#fff" stroke-width="1.3"/><path d="M1 3 L6 7 L11 3" fill="none" stroke="#fff" stroke-width="1.3"/></svg></span>sales@larkvalecoilworks.com.au</div>
    <div class="contact__line"><span class="icon"><svg width="12" height="12" viewBox="0 0 12 12"><circle cx="6" cy="6" r="4.5" fill="none" stroke="#fff" stroke-width="1.2"/><ellipse cx="6" cy="6" rx="2" ry="4.5" fill="none" stroke="#fff" stroke-width="1"/><path d="M1.5 6 H10.5" stroke="#fff" stroke-width="1"/></svg></span>www.larkvalecoilworks.com.au</div>
  </div>
  <div class="callout">Call Us! 1300 555 274</div>
</section>

<section class="card card--back">
  <div class="gallery">
    <div class="panel panel--kit"><div class="panel__photo photo--kit" role="img" aria-label="Product photo of the chrome lock cups and installation tool set"></div></div>
    <div class="panel panel--tool"><div class="panel__photo photo--tool" role="img" aria-label="Product photo of the bolt puller tool with lock cup and key"></div></div>
    <div class="panel panel--pack"><div class="panel__photo photo--pack" role="img" aria-label="Product photo of the boxed starter pack with instructions"></div></div>
  </div>
  <div class="tread" style="left:455px;top:190px;width:245px;height:66px"></div>
  <div class="brand">
    <span class="brand__origin">Made In Australia</span>
    <span class="brand__name"><span class="brand__mark"></span>Larkvale</span>
    <span class="brand__tag">Coil Starter Pack</span>
  </div>
  <div class="badge" aria-hidden="true"></div>
  <div class="fitment">Suits<strong>KR-KT ARLEN</strong><strong>MX-MY TALLOW</strong>(2002-Mid 2008)</div>
  <svg class="band" viewBox="0 0 700 400" aria-hidden="true">
    <path d="M0 382 L330 372 C470 360 600 345 700 320 L700 400 L0 400 Z" fill="var(--red)"/>
    <path d="M0 374 L330 364 C470 352 600 337 700 312" fill="none" stroke="var(--ink)" stroke-width="3"/>
  </svg>
  <div class="site">www.larkvalecoilworks.com.au</div>
</section>

</body>
</html>
```